Stoneline Benchworks Australia - Pool Flyer

G'day,Stoneline Benchworks Australia sells poolforms (https://www.stonelinebenchworksaustralia.com.au/index.php?route=product/category&path=17_61) The poolforms are reusable forms to pour a seamless concrete pool surround instead of using coping tiles. A much better look, less maintenance, and a modern architectural look .We're going to attend a pool and spa show but it is also about landscaping/surround as well. The forms we do make the concrete surround of a pool instead of tiles. I've put some text in a word doc and pictures as well. Feel free to use any words from our website and use/crop pics as you see fit.Any questions, more than happy to answer. We're thinking an A4 tri-fold flyer but happy for other suggestions as well. We're going to attend the show, speak to exhibitors, and hand them the flyer (and maybe a little promo thing too).

Target Market(s)

The target market is we are going to a pool and spa expo. The exhibitors install pools and do backyard landscaping. The flyer is for them.

Colors

Designer to choose colors to be used in the design.

Requirements
Must have
• The text/description of the poolforms and some of the pictures.
• Finished pictures.
• 1 or 2 of the forms (From the website).
• 1 of the Veil skimmer cap pictures (finished is probably better from the jpg with 3 images. probably best to crop and use 1 of the 3.
• Contact details of the website & email contact of sales@stonelinebenchworksaustralia.com.au + the phone number.

```html
<!DOCTYPE html>
<html lang="en">
<head>
<meta charset="utf-8">
<title>Stoneline Benchworks Australia – Pool Flyer</title>
<link rel="stylesheet" href="https://fonts.googleapis.com/css2?family=Roboto+Slab:wght@500;600;700&family=Lato:ital,wght@0,400;0,700;1,400&display=swap">
<style>
  :root{
    --stage:#3a3a3a;
    --sky:#8fd3f4;
    --sky-light:#c4e8fa;
    --ocean:#1a95d3;
    --ocean-deep:#1577b0;
    --sun:#f8b422;
    --ink:#1d3a52;
    --ink-soft:#22313d;
    --call:#1a8bcc;
    --white:#ffffff;
  }
  *{box-sizing:border-box;margin:0;padding:0}
  html,body{width:1200px;height:1092px;overflow:hidden;background:var(--stage)}
  .flyer{position:absolute;left:232px;top:26px;width:735px;height:1040px;background:var(--sky);overflow:hidden;box-shadow:0 10px 30px rgba(0,0,0,.45)}
  .flyer__art{position:absolute;inset:0;width:735px;height:1040px}
  .brand{position:absolute;left:30px;top:378px;display:flex;align-items:center;gap:10px}
  .brand__dot{width:24px;height:24px;border-radius:50%;background:var(--ink)}
  .brand__name{font:600 11px/1.35 "Roboto Slab",serif;letter-spacing:3px;color:var(--ink);text-transform:uppercase;width:150px}
  .title{position:absolute;left:30px;top:452px;font:500 24px/1.22 "Roboto Slab",serif;color:var(--ink)}
  .title-rule{position:absolute;left:32px;top:518px;width:240px;height:3px;background:var(--white)}
  .call{position:absolute;left:32px;top:530px;font:700 22px/1.2 "Lato",sans-serif;color:var(--call)}
  .web{position:absolute;left:32px;top:560px;font:700 14.5px/1.2 "Lato",sans-serif;color:var(--call)}
  .pitch{position:absolute;left:41px;top:622px;width:360px}
  .pitch__heading{font:600 21.5px/1.05 "Roboto Slab",serif;color:#151d24}
  .pitch__body{margin-top:8px;font:400 12.2px/1.22 "Lato",sans-serif;color:var(--ink-soft)}
  .adv{position:absolute;left:43px;top:750px;width:330px}
  .adv__heading{font:600 17.5px/1 "Roboto Slab",serif;letter-spacing:1px;color:#151d24;text-transform:uppercase}
  .adv__rule{width:108px;height:3px;background:var(--ocean);margin-top:6px}
  .adv__list{list-style:none;margin-top:13px}
  .adv__item{position:relative;padding-left:23px;font:italic 400 10.2px/1.28 "Lato",sans-serif;color:#15202a;margin-bottom:10px}
  .adv__item svg{position:absolute;left:0;top:0;width:12px;height:12px}
</style>
</head>
<body>
<main class="flyer">
  <svg class="flyer__art" viewBox="0 0 735 1040" xmlns="http://www.w3.org/2000/svg">
    <defs>
      <linearGradient id="poolPhoto" x1="0" y1="0" x2="1" y2="1">
        <stop offset="0" stop-color="#5d7d6a"/><stop offset=".35" stop-color="#d9e2e6"/>
        <stop offset=".55" stop-color="#2f62c8"/><stop offset=".8" stop-color="#1f3a5e"/><stop offset="1" stop-color="#c9c9c4"/>
      </linearGradient>
      <linearGradient id="divePhoto" x1="0" y1="0" x2="0" y2="1">
        <stop offset="0" stop-color="#6f7a5e"/><stop offset=".55" stop-color="#9a958a"/><stop offset="1" stop-color="#2bb6d8"/>
      </linearGradient>
      <linearGradient id="plungePhoto" x1="0" y1="0" x2="0" y2="1">
        <stop offset="0" stop-color="#1e2a22"/><stop offset=".45" stop-color="#1d3fb0"/><stop offset="1" stop-color="#c8c2b6"/>
      </linearGradient>
      <linearGradient id="lidPhoto" x1="0" y1="0" x2="1" y2="1">
        <stop offset="0" stop-color="#a7a9ab"/><stop offset="1" stop-color="#86898c"/>
      </linearGradient>
      <linearGradient id="edgePhoto" x1="0" y1="0" x2="1" y2="1">
        <stop offset="0" stop-color="#dcd3c6"/><stop offset=".7" stop-color="#c9c2b8"/><stop offset="1" stop-color="#2a5fc0"/>
      </linearGradient>
      <linearGradient id="bucketPhoto" x1="0" y1="0" x2="0" y2="1">
        <stop offset="0" stop-color="#d9d6d0"/><stop offset=".6" stop-color="#6a4a2a"/><stop offset="1" stop-color="#c6c4bf"/>
      </linearGradient>
    </defs>

    <!-- hero photo -->
    <rect class="hero" x="0" y="0" width="735" height="360" fill="url(#poolPhoto)" role="img" aria-label="Photo: long resort lap pool with seamless concrete edge and sun loungers"/>

    <!-- top wave bands -->
    <path fill="var(--sun)" d="M0 338 C60 322 120 350 190 336 C260 322 330 350 400 334 C470 320 540 346 610 332 C670 322 710 340 735 330 L735 380 L0 380 Z"/>
    <path fill="var(--ocean)" d="M0 352 C60 338 120 364 190 350 C260 336 330 364 400 348 C470 334 540 360 610 346 C670 336 710 354 735 344 L735 390 L0 390 Z"/>
    <path fill="var(--sky)" d="M0 358 C60 346 120 370 190 357 C260 344 330 370 400 355 C470 342 540 367 610 353 C670 344 710 361 735 352 L735 1040 L0 1040 Z"/>

    <!-- lighter feature area -->
    <path fill="var(--sky-light)" d="M0 598 C120 570 300 560 430 592 C560 625 640 720 650 830 C660 920 640 960 620 1000 L0 1000 Z"/>

    <!-- octagon photos -->
    <g transform="translate(548 371)">
      <polygon fill="var(--ocean)" points="101.6,42.1 42.1,101.6 -42.1,101.6 -101.6,42.1 -101.6,-42.1 -42.1,-101.6 42.1,-101.6 101.6,-42.1"/>
      <polygon fill="url(#divePhoto)" role="img" aria-label="Photo: swimmer diving into a backyard pool" points="90.5,37.5 37.5,90.5 -37.5,90.5 -90.5,37.5 -90.5,-37.5 -37.5,-90.5 37.5,-90.5 90.5,-37.5"/>
    </g>
    <g transform="translate(554 580)">
      <polygon fill="var(--ocean)" points="97.9,40.6 40.6,97.9 -40.6,97.9 -97.9,40.6 -97.9,-40.6 -40.6,-97.9 40.6,-97.9 97.9,-40.6"/>
      <polygon fill="url(#plungePhoto)" role="img" aria-label="Photo: plunge pool with seamless exposed aggregate surround" points="86.8,36 36,86.8 -36,86.8 -86.8,36 -86.8,-36 -36,-86.8 36,-86.8 86.8,-36"/>
    </g>

    <!-- circle photos -->
    <circle cx="634" cy="757" r="68" fill="var(--ocean)"/>
    <circle cx="634" cy="757" r="61" fill="url(#edgePhoto)" role="img" aria-label="Photo: veil skimmer cap set into a honed concrete pool edge"/>
    <circle cx="509" cy="783" r="72" fill="#7fc9ef"/>
    <circle cx="509" cy="783" r="65" fill="url(#lidPhoto)" role="img" aria-label="Photo: veil skimmer cap flush in grey concrete"/>
    <circle cx="552" cy="897" r="91" fill="#7fc9ef"/>
    <circle cx="552" cy="897" r="83" fill="url(#bucketPhoto)" role="img" aria-label="Photo: drinks chilling in ice on a concrete surround"/>

    <!-- bottom wave bands -->
    <path fill="var(--ocean)" d="M0 978 C70 964 140 992 220 978 C300 964 370 990 450 976 C530 962 600 988 680 974 C710 969 725 972 735 970 L735 1040 L0 1040 Z"/>
    <path fill="var(--sun)" d="M0 1006 C70 996 140 1018 220 1006 C300 994 370 1016 450 1004 C530 992 600 1014 680 1002 C710 998 725 1000 735 998 L735 1040 L0 1040 Z"/>
  </svg>

  <div class="brand">
    <span class="brand__dot"></span>
    <span class="brand__name">Stoneline Benchworks Australia</span>
  </div>

  <h1 class="title">Stoneline Benchworks<br>Australia-Pool Flyer</h1>
  <div class="title-rule"></div>
  <p class="call">Call US Now: 1300-762-419</p>
  <p class="web">Website : www.stonelinebenchworksaustralia.com</p>

  <section class="pitch">
    <h2 class="pitch__heading">The best seamless pooledge<br>forming system</h2>
    <p class="pitch__body">Don't waste your time with fiddly, flimsy, or time consuming pool edge forming systems that end up in landfill. The SL poolforms are made from strong PVC and can produce architectural designed looks that suit all types of pools.</p>
  </section>

  <section class="adv">
    <h2 class="adv__heading">Advantages</h2>
    <div class="adv__rule"></div>
    <ul class="adv__list">
      <li class="adv__item"><svg viewBox="0 0 12 12"><rect width="12" height="12" rx="1.5" fill="#1a95d3"/><path d="M2.8 6.2 5 8.4 9.3 3.8" fill="none" stroke="#fff" stroke-width="1.6"/></svg>Form and pour a seamless concrete pool surround.</li>
      <li class="adv__item"><svg viewBox="0 0 12 12"><rect width="12" height="12" rx="1.5" fill="#1a95d3"/><path d="M2.8 6.2 5 8.4 9.3 3.8" fill="none" stroke="#fff" stroke-width="1.6"/></svg>Architectural-designed look.</li>
      <li class="adv__item"><svg viewBox="0 0 12 12"><rect width="12" height="12" rx="1.5" fill="#1a95d3"/><path d="M2.8 6.2 5 8.4 9.3 3.8" fill="none" stroke="#fff" stroke-width="1.6"/></svg>Virtually no maintenance.</li>
      <li class="adv__item"><svg viewBox="0 0 12 12"><rect width="12" height="12" rx="1.5" fill="#1a95d3"/><path d="M2.8 6.2 5 8.4 9.3 3.8" fill="none" stroke="#fff" stroke-width="1.6"/></svg>Easy to use to create a seamless pooledge.</li>
      <li class="adv__item"><svg viewBox="0 0 12 12"><rect width="12" height="12" rx="1.5" fill="#1a95d3"/><path d="M2.8 6.2 5 8.4 9.3 3.8" fill="none" stroke="#fff" stroke-width="1.6"/></svg>Made from tough PVC.</li>
      <li class="adv__item"><svg viewBox="0 0 12 12"><rect width="12" height="12" rx="1.5" fill="#1a95d3"/><path d="M2.8 6.2 5 8.4 9.3 3.8" fill="none" stroke="#fff" stroke-width="1.6"/></svg>Any Type of Concrete - Honed Aggregate, Exposed Aggregate,<br>Grey or any colour concrete.</li>
      <li class="adv__item"><svg viewBox="0 0 12 12"><rect width="12" height="12" rx="1.5" fill="#1a95d3"/><path d="M2.8 6.2 5 8.4 9.3 3.8" fill="none" stroke="#fff" stroke-width="1.6"/></svg>Double sided Polyester mounting tape used to fasten Receiver.<br>Track (SB-204) to top of fiberglass or gunnite pool.</li>
    </ul>
  </section>
</main>
</body>
</html>
```